Book Cover (QUIET WEEKS MEND EVERY KNOT)

This book is a series of blog posts from my blog, Sparks Kept Handy, which is at glenferrante.example/blog.
The book is to be called:
QUIET WEEKS MEND EVERY KNOT
And 51 other Sparks Kept Handy from the Corner Shop Tutor
(Sparks Kept Handy) should be italicized.
My name is Glen Ferrante, M.B.A.

I will need three variations for my paperback, hardcover and e-book.
Here are some of the blog titles and their topics:
Preparing Your Small Business For Recession small business recession
Should I Incorporate My Business? Should I Incorporate My Business?
Alternative to Minority Shareholder In Small Private Companies minority shareholder
Small Business Culture – Getting it Right Small Business Culture
What is The Right Way to Fire Someone The Right Way to Fire Someone
The Five Basic Leadership Principles Leadership Principles
10 Tips for New Entrepreneurs – Sure Ways to Increase Your Chances of Success
10 things to consider before becoming an entrepreneur
Strategy vs Biz Plans small business strategy
Closing Sales close the sale
Breakeven break even
Growth makes cash flow suck cash flow issues
Think Twice About Offering Early Payment Discounts prepayment discounts
Firing Customers firing customers
Collections best practices getting paid faster
The Cash Flow Statement cash flow statement
Using Paralegals paralegal
Radical Candor radical candor
Why No is the Second Best Word to a Salesperson's ears value of no
The $8 Million Problem -
Contractor vs Employee contractor vs employee
The Columbo sales tactic
Systems Turn Goals From Dreams Into Reality Systems vs Goals
The Importance of Realistic Goals stretch goals
Why The Owner Must Review Every Hire hiring for values
Systems Thinking for Small Biz: The Case for SOPs systems thinking
Trust Your Gut business intuition
Grease and friction grease vs friction
Left alone, 90% of problems solve themselves strategic inaction
Referrals Are Great—But Not a Growth Strategy referrals
The Lean Marketing Machine: 7 Hacks to Grow Your Small Business Fast marketing hacks
The Small Business Health Check small business health check
How to Spot a Customer Headed for Trouble — Before They Take You Down With Them customer warning signs
We Are What We Repeatedly Do habits
The Smartest People Know When to Play Dumb playing dumb
Before You Scale, Do the Math unit economics
AI for Small Business: Practical Tools and Use Cases AI for Small Business
Title: Tell Me Right Now—Why Can’t We Raise Your Prices? small business pricing
Why Your Real Competitor Isn’t Who You Think creative destruction
Good Enough Might Be Great satisficing
Bootstrapping: Building Your Business on Your Terms bootstrapping
Building Resilient Companies That Never Have to Bet the Farm bet the farm
We Always Overshoot: From Fiber to Cannabis to AI AI overbuild
A Bias Toward Action bias toward ation
Choosing the Right Business Owner Title business owner title
Jobs to Be Done: Understanding What Your Customers Really Want Jobs to Be Done
Forget Money. Here’s What Really Motivates People. motivation

Target Market(s)

Small business operators, business school students

Industry/Entity Type

Small business

Colors

Designer to choose colors to be used in the design.

Requirements
Should not have
• Should not look cartoonish

```html
<!DOCTYPE html>
<html lang="en">
<head>
<meta charset="utf-8">
<title>Quiet Weeks Mend Every Knot — Book Cover</title>
<link href="https://fonts.googleapis.com/css2?family=Roboto+Condensed:ital,wght@0,400;0,700;1,400&display=swap" rel="stylesheet">
<style>
  :root {
    --backdrop: #e4e4e4;
    --navy: #1f4a7c;
    --navy-deep: #17406f;
    --paper: #d8d8d6;
    --ink: #1c1c1c;
    --white: #ffffff;
    --rule: rgba(255,255,255,0.55);
    --tangle-red: rgba(214,51,44,0.22);
    --bulb-green: rgba(123,211,52,0.30);
  }
  * { margin: 0; padding: 0; box-sizing: border-box; }
  html, body {
    width: 1200px; height: 1200px; overflow: hidden;
    background: var(--backdrop);
  }
  .cover {
    position: absolute; left: 250px; top: 41px;
    width: 700px; height: 1117px;
    background: var(--paper);
    font-family: "Roboto Condensed", "Arial Narrow", sans-serif;
    overflow: hidden;
  }
  .cover__top {
    position: absolute; left: 0; top: 0; width: 100%; height: 527px;
    background: linear-gradient(180deg, var(--navy) 0%, var(--navy-deep) 100%);
  }
  .cover__pointer {
    position: absolute; left: 309px; top: 526px;
  }
  .title {
    position: absolute; left: 0; top: 112px; width: 100%;
    text-align: center; color: var(--white);
    font-weight: 700; font-size: 76px; line-height: 108px;
    letter-spacing: 1px; white-space: nowrap;
  }
  .title__rule {
    position: absolute; left: 121px; top: 350px;
    width: 458px; height: 2px; background: var(--rule);
  }
  .subtitle {
    position: absolute; left: 0; top: 384px; width: 100%;
    text-align: center; color: var(--white);
    font-weight: 400; font-size: 28px; line-height: 42px;
  }
  .subtitle__series { font-style: italic; }
  .artwork {
    position: absolute; left: 0; top: 660px; width: 100%; height: 190px;
    background: linear-gradient(90deg,
      var(--paper) 0%, var(--tangle-red) 25%, var(--tangle-red) 40%,
      var(--paper) 58%, var(--paper) 72%, var(--bulb-green) 92%, var(--paper) 100%);
  }
  .author {
    position: absolute; left: 0; top: 930px; width: 100%;
    text-align: center; color: var(--ink);
    font-weight: 700; font-size: 50px;
  }
  .web {
    position: absolute; left: 0; top: 1027px; width: 100%;
    text-align: center; color: var(--ink);
    font-weight: 400; font-size: 24px;
  }
</style>
</head>
<body>
  <main class="cover">
    <div class="cover__top"></div>
    <svg class="cover__pointer" width="82" height="42" viewBox="0 0 82 42" aria-hidden="true">
      <polygon points="0,0 82,0 41,42" fill="#17406f"/>
    </svg>

    <h1 class="title">QUIET WEEKS<br>MEND EVERY KNOT</h1>
    <div class="title__rule"></div>
    <p class="subtitle">And 51 other <em class="subtitle__series">Sparks Kept Handy</em><br>from the Corner Shop Tutor</p>

    <div class="artwork" role="img" aria-label="Illustration of a tangled red line that straightens into white paths leading to a glowing green light bulb"></div>

    <p class="author">Glen Ferrante, M.B.A</p>
    <p class="web">glenferrante.example/blog</p>
  </main>
</body>
</html>
```